Microlight Aircraft Website Project

Need a website designed, or at least a template made, that my web programmer can work with here. We are a new manufacturer of microlight aircraft & powered hang gliders. Our company name is Brisk Fern. We manufacture portable utility aircraft in the Light Sport category (formerly known as Ultralights or Microlights). Our particular design is a 2-seat powered hang glider and caters to those who want to go explore the backcountry. We are not necessarily aviation nuts, but more into the development of a flying utility vehicle for extreme exploration and expeditions. We have been importing these aircraft from 3 countries for 15 years and have supplied over 200 expedition-quality aircraft world-wide. We are now manufacturing here in the US.

Industry/Entity Type

Manufacturer

Coding

Coded - Design and coding required

```html
<!DOCTYPE html>
<html lang="en">
<head>
<meta charset="utf-8">
<title>Brisk Fern</title>
<link href="https://fonts.googleapis.com/css2?family=Signika:wght@300;400;600;700&display=swap" rel="stylesheet">
<style>
:root{
  --navy:#0b4f99;
  --navy-dark:#0a3f86;
  --sky:#27aae1;
  --grey-band:#f1f1f1;
  --circle:#ebebeb;
  --text:#5b6066;
  --nav:#6b6f74;
  --white:#ffffff;
}
*{margin:0;padding:0;box-sizing:border-box}
html,body{width:692px;height:1200px;overflow:hidden;background:var(--white)}
body{font-family:"Signika",sans-serif;color:var(--text);position:relative;font-weight:300}
.abs{position:absolute}
.shapes{position:absolute;left:0;top:0}
/* header */
.brand{left:76px;top:16px;display:flex;align-items:center;gap:7px}
.brand-dot{width:22px;height:22px;border-radius:50%;background:var(--navy)}
.brand-name{font-size:18px;font-weight:700;color:var(--navy);letter-spacing:.2px}
.nav{left:254px;top:9px;display:flex;gap:13px;font-size:6.4px;font-weight:400;color:var(--nav);text-transform:uppercase}
.nav .active{color:var(--navy);border-bottom:1px solid var(--navy)}
.mail{right:76px;top:29px;font-size:7.5px;font-weight:400;color:var(--white);display:flex;align-items:center;gap:4px}
/* hero */
.hero-copy{left:0;width:692px;top:155px;text-align:center;color:var(--white)}
.hero-title{font-size:21px;font-weight:700;letter-spacing:.3px}
.hero-text{font-size:6.4px;font-weight:400;line-height:11px;margin-top:6px}
.hero-btn{display:inline-block;margin-top:14px;border:1.5px solid var(--white);padding:8px 11px;font-size:6.5px;font-weight:400}
.slider-dots{display:flex;gap:9px}
.slider-dots span{width:4.5px;height:4.5px;border-radius:50%;background:var(--white)}
.slider-dots span.on{background:transparent;border:1px solid var(--white)}
.hero-aircraft{left:92px;top:284px;width:184px;height:116px;background:linear-gradient(135deg,#2e3a78,#3d4f8c 50%,#d8c63a)}
/* sections */
.section-title{left:0;width:692px;text-align:center;font-size:21px;font-weight:700;letter-spacing:.3px}
.navy{color:var(--navy)}
.sky{color:var(--sky)}
.welcome-text{left:76px;width:540px;top:427px;text-align:center;font-size:5.5px;line-height:11px}
.product{width:247px;text-align:center}
.product-photo{width:247px;height:154px}
.product-name{font-size:11px;color:var(--sky);margin-top:8px;font-weight:300}
.product-text{font-size:6.4px;line-height:11px;margin-top:5px}
.gallery{left:76px;top:875px;display:grid;grid-template-columns:repeat(4,126px);column-gap:11.5px;row-gap:11px}
.gallery div{height:91px}
.gallery-dots{left:328px;top:1090px;display:flex;gap:8px}
.gallery-dots span{width:5px;height:5px;border-radius:50%;background:#c8c8c8}
.gallery-dots span.on{background:#7fcbe0}
/* footer */
.foot-brand{left:76px;top:1143px;display:flex;align-items:center;gap:6px}
.foot-brand .brand-dot{width:17px;height:17px;background:#7ea9d8}
.foot-brand .brand-name{font-size:12px;color:#9fc0e6}
.social{left:542px;top:1137px;display:flex;gap:13px}
.social span{width:8px;height:8px;border-radius:50%;background:var(--white)}
.foot-links{left:76px;top:1175px;font-size:5.8px;font-weight:400;color:var(--white);display:flex;gap:5px}
.foot-links i{font-style:normal;opacity:.7}
.copyright{right:76px;top:1175px;font-size:5.8px;font-weight:400;color:var(--white)}
</style>
</head>
<body>

<svg class="shapes" width="692" height="1200" viewBox="0 0 692 1200">
  <defs>
    <linearGradient id="heroTone" x1="0" y1="0" x2="1" y2="1">
      <stop offset="0" stop-color="#1ab5e8"/>
      <stop offset=".55" stop-color="#27c4ec"/>
      <stop offset="1" stop-color="#1d6c8c"/>
    </linearGradient>
  </defs>
  <circle cx="205" cy="282" r="123" fill="var(--circle)"/>
  <polygon points="0,62 692,36 692,385 0,322" fill="url(#heroTone)" role="img" aria-label="Aerial view of turquoise bay with forested islands"/>
  <polygon points="345,34 692,0 692,60 520,62" fill="var(--navy)"/>
  <polygon points="0,500 164,480 344,510 524,480 692,512 692,800 0,800" fill="var(--grey-band)"/>
  <rect x="0" y="1116" width="692" height="84" fill="var(--navy)"/>
  <polygon points="350,1120 692,1116 692,1165" fill="var(--sky)"/>
</svg>

<div class="abs hero-aircraft" role="img" aria-label="Powered hang glider trike in flight"></div>

<div class="abs brand"><span class="brand-dot"></span><span class="brand-name">BRISK FERN</span></div>
<nav class="abs nav"><span class="active">Home</span><span>Products</span><span>Gallery</span><span>About us</span><span>Contact us</span></nav>
<div class="abs mail">
  <svg width="8" height="6" viewBox="0 0 8 6"><rect x=".5" y=".5" width="7" height="5" fill="none" stroke="#fff"/><path d="M.5 .5 L4 3.3 L7.5 .5" fill="none" stroke="#fff"/></svg>
  hello@briskfern-air.example
</div>

<div class="abs hero-copy">
  <h1 class="hero-title">MAURIS AUCTOR TINCIDUNT</h1>
  <p class="hero-text">Nullam eu pulvinar nisl. Vestibulum lacinia dui vitae odio aliquam, a blandit neque tincidunt.<br>Cras varius suscipit tristique. In ac ligula sagittis, feugiat libero at, facilisis eros.</p>
  <span class="hero-btn">VIEW MORE</span>
</div>
<div class="abs slider-dots" style="left:322px;top:334px"><span class="on"></span><span></span><span></span><span></span></div>

<h2 class="abs section-title navy" style="top:395px">WELCOME</h2>
<p class="abs welcome-text">Sed pretium in ante non imperdiet. Sed vel rutrum erat, et consectetur neque. Curabitur ut risus arcu. Suspendisse potenti. Nunc erat lectus, dignissim dictum sem sit amet, faucibus condimentum massa. Curabitur eleifend metus in diam varius maximus. Cras lacinia, risus non sollicitudin tincidunt, diam nisl fringilla metus, at laoreet ex mauris a arcu. Vivamus id neque at elit tempus congue rhoncus vitae elit. Maecenas pretium sapien augue, non vestibulum diam iaculis et. Nulla eu dapibus felis, vitae faucibus sem. Mauris imperdiet purus ut hendrerit luctus.</p>

<h2 class="abs section-title sky" style="top:537px">OUR PRODUCTS</h2>
<div class="abs product" style="left:85px;top:573px">
  <div class="product-photo" role="img" aria-label="Microlight aircraft with red wing against blue sky" style="background:linear-gradient(160deg,#8cc6ee,#4fa0dd)"></div>
  <h3 class="product-name">Microlight Aircraft</h3>
  <p class="product-text">Donec ultrices tortor id varius porta. Nullam placerat lobortis orci, ut hen drerit tortor aliquet ac. Nunc convallis nec nulla eget gravida.</p>
</div>
<div class="abs product" style="left:359px;top:573px">
  <div class="product-photo" role="img" aria-label="Powered paraglider with yellow canopy among clouds" style="background:linear-gradient(200deg,#5d8fbf,#dfe6ee 55%,#9ab4cf)"></div>
  <h3 class="product-name">Powered Hang Gliders</h3>
  <p class="product-text">Donec ultrices tortor id varius porta. Nullam placerat lobortis orci, ut hen drerit tortor aliquet ac. Nunc convallis nec nulla eget gravida.</p>
</div>

<h2 class="abs section-title navy" style="top:836px">GALLERY</h2>
<div class="abs gallery">
  <div role="img" aria-label="Trikes parked on an airfield" style="background:linear-gradient(180deg,#a9b6c0,#b9a27c)"></div>
  <div role="img" aria-label="Yellow hang glider in blue sky" style="background:#4f86cf"></div>
  <div role="img" aria-label="Paraglider with turquoise canopy" style="background:#4f79cd"></div>
  <div role="img" aria-label="Trike taking off from dry field" style="background:linear-gradient(180deg,#c9d9ea,#a68a6c)"></div>
  <div role="img" aria-label="Paramotor pilot under canopy" style="background:#5a7ccc"></div>
  <div role="img" aria-label="Pilot in helmet before flight" style="background:linear-gradient(135deg,#3b3b3b,#c8c0a8)"></div>
  <div role="img" aria-label="Trike with red wing in flight" style="background:#5a86d4"></div>
  <div role="img" aria-label="Paraglider over mountains" style="background:linear-gradient(180deg,#5a9ad6,#c6d8e6)"></div>
</div>
<div class="abs gallery-dots"><span class="on"></span><span></span><span></span></div>

<div class="abs foot-brand"><span class="brand-dot"></span><span class="brand-name">BRISK FERN</span></div>
<div class="abs social" aria-label="Social links"><span></span><span></span><span></span><span></span></div>
<div class="abs foot-links"><span>Home</span><i>|</i><span>Products</span><i>|</i><span>Gallery</span><i>|</i><span>About us</span><i>|</i><span>Contact us</span></div>
<div class="abs copyright">Copyright © 2016 Brisk Fern. &nbsp;All rights reserved.</div>

</body>
</html>
```